Metal head/ Sushi chef wanting artistic yet high imact business card

I'm sushi chef for make living in Australia originally from Tokyo Japan.
I'm also guitarist/composer as well on progressive metalcore/djent genre.
My favorite visual art is Mandala. Sacred geometries, Fractals, Paisleys are also things fit in me. I like dark color, earth color, and sometimes psychedelic patterns.
I want to hand out my business card when I meet new people in music industries or someone who is wanting private sushi chef for their party.
I know metal and sushi are far different subjects but they are all my passion. I would like to work with the designer who can create something cool from information above.

https://www.viewtrove.com/channel/QX7h4LpRzd2VnWe9kT3BFs8j
https://tunebarrel.com/user-817264093

Front
my name, Kenjiro Motsuba
occupation, "Sushi chef" "Metal guitarist/composer"
Email address, velmoquartz@mailorb.com
Phone number, (61)498271053

Back:
My Viewtrove channel, Pagefolk, Tunebarrel, Glintory. All of those are searchable by "Velmoquartz" The website mentioned above can be described as their logos.

Target Market(s)

people in Music industry, such as musicians, venue managers, promoters.
People who wants to have private sushi chef for their private function, party or events.

Industry/Entity Type

Artists

Contact Information for Business Card

Uploaded photos are just image reference. not thinking to use them.
My details:
I like :
energetic music that has a lot of details such as Progressive metalcore, jazz, djent, psychedelic music.
Spiritual thoughs, Buddism, fundamentals, relaxation music, 420, weed culture, Free thoughts
U.S street culture, skate board, kelps, surf, bicycle, nature, camping, hiking, ocean, mountain, desert, countryside,
permaculture, natural farming, organic farming, compost, self sufficient.
nigiri sushi, art sushi, something/someone beautiful in mind.

Dislike:
Fakes, Bullshits, format, negative, preservatives, artificial colors, illuminati, satanism, manipulation, mass favorites, big society, politics, Chinese letters on western design

Colors
0455a3
000000
7c7c7c
00a990
acd036
f37122

Requirements
Must have
• Front
• my name, Kenjiro Motsuba
• occupation, "Sushi chef" "Metal guitarist/composer"
• Email address, velmoquartz@mailorb.com
• Phone number, (61)498271053
• Back:
• My Viewtrove channel, Pagefolk, Tunebarrel, Glintory. All of those are searchable by "Velmoquartz" The website mentioned above can be described as their logos.
Nice to have
• something based on one of those either back ground or logo:
• Mandala, Sacred Geometry, Fractal art
Should not have
• pop essence. mass favorites, pink, Chinese letters, asian fonts, something asian

```html
<!DOCTYPE html>
<html lang="en">
<head>
<meta charset="utf-8">
<title>Kenjiro Motsuba — Business Card</title>
<link rel="stylesheet" href="https://fonts.googleapis.com/css2?family=Montserrat:wght@200;300;800&display=swap">
<style>
  :root {
    --backdrop: #d6d5cf;
    --card-teal: #00a990;
    --accent-lime: #acd036;
    --ink: #000000;
    --handle-ink: #0b5f52;
  }
  * { box-sizing: border-box; margin: 0; padding: 0; }
  html, body { width: 1200px; height: 1200px; overflow: hidden; }
  body {
    background: var(--backdrop);
    font-family: "Montserrat", sans-serif;
    display: flex;
    flex-direction: column;
    align-items: center;
    justify-content: center;
    gap: 60px;
  }
  .card {
    position: relative;
    width: 880px;
    height: 500px;
    background: var(--card-teal);
    overflow: hidden;
  }
  .card-frame {
    position: absolute;
    inset: 34px 40px;
    border: 2px solid var(--ink);
  }
  .ornament {
    position: absolute;
    width: 190px;
    height: 190px;
    border-radius: 50%;
    background: radial-gradient(circle, rgba(172,208,54,0.85) 0%, rgba(172,208,54,0.55) 45%, rgba(172,208,54,0.25) 70%, rgba(172,208,54,0) 72%);
  }
  .ornament--top-left { left: -80px; top: -70px; }
  .ornament--right { right: -90px; top: 120px; }

  /* Front */
  .identity {
    position: absolute;
    left: 330px;
    top: 120px;
    width: 340px;
    text-align: center;
    color: var(--ink);
  }
  .identity-name { font-weight: 800; font-size: 27px; letter-spacing: 0.2px; }
  .identity-role { font-weight: 300; font-size: 19px; line-height: 1.3; margin-top: 10px; }
  .identity-mark {
    margin-top: 22px;
    color: var(--accent-lime);
    font-weight: 800;
    font-size: 24px;
  }
  .contact {
    position: absolute;
    color: var(--ink);
    font-weight: 300;
    font-size: 19px;
    text-align: center;
  }
  .contact svg { display: block; margin: 0 auto 6px; }
  .contact--email { left: 90px; top: 340px; }
  .contact--phone { right: 90px; top: 400px; }

  /* Back */
  .social-list {
    position: absolute;
    left: 88px;
    top: 70px;
    list-style: none;
    display: flex;
    flex-direction: column;
    gap: 38px;
  }
  .social-item {
    display: flex;
    align-items: center;
    gap: 10px;
    color: var(--accent-lime);
    font-weight: 800;
    font-size: 17px;
  }
  .social-item::before {
    content: "";
    width: 34px;
    height: 34px;
    border-radius: 8px;
    background: var(--accent-lime);
  }
  .handle-rule {
    position: absolute;
    left: 295px;
    top: 60px;
    width: 5px;
    height: 300px;
    background: var(--ink);
  }
  .handle-rule::after {
    content: "";
    position: absolute;
    left: 0;
    top: 148px;
    width: 26px;
    height: 5px;
    background: var(--ink);
  }
  .handle {
    position: absolute;
    left: 340px;
    top: 190px;
    font-weight: 200;
    font-size: 34px;
    letter-spacing: 1px;
    color: var(--handle-ink);
    white-space: nowrap;
  }
  .back-mark {
    position: absolute;
    right: 90px;
    top: 300px;
    color: var(--accent-lime);
    font-weight: 800;
    font-size: 30px;
    white-space: nowrap;
  }
</style>
</head>
<body>

  <section class="card card--front">
    <div class="card-frame"></div>
    <div class="ornament ornament--top-left" role="img" aria-label="Lime mandala ornament"></div>
    <div class="ornament ornament--right" role="img" aria-label="Lime mandala ornament"></div>

    <div class="identity">
      <h1 class="identity-name">Kenjiro Motsuba</h1>
      <p class="identity-role">Sushi chef<br>Metal Guitarist / Composer</p>
      <p class="identity-mark">Velmoquartz</p>
    </div>

    <div class="contact contact--email">
      <svg width="30" height="22" viewBox="0 0 30 22" aria-hidden="true">
        <rect x="1" y="1" width="28" height="20" fill="var(--accent-lime)"/>
        <path d="M1 1 L15 12 L29 1" fill="none" stroke="var(--card-teal)" stroke-width="2"/>
      </svg>
      velmoquartz@mailorb.com
    </div>

    <div class="contact contact--phone">
      <svg width="14" height="24" viewBox="0 0 14 24" aria-hidden="true">
        <rect x="1" y="1" width="12" height="22" rx="2" fill="none" stroke="var(--accent-lime)" stroke-width="2"/>
        <line x1="5" y1="19" x2="9" y2="19" stroke="var(--accent-lime)" stroke-width="2"/>
      </svg>
      (61)498271053
    </div>
  </section>

  <section class="card card--back">
    <div class="card-frame"></div>
    <ul class="social-list">
      <li class="social-item">Viewtrove</li>
      <li class="social-item">Glintory</li>
      <li class="social-item">Pagefolk</li>
      <li class="social-item">Tunebarrel</li>
    </ul>
    <div class="handle-rule"></div>
    <p class="handle">Velmoquartz</p>
    <p class="back-mark">Velmoquartz</p>
  </section>

</body>
</html>
```